Verpackungen - Umkarton für den ersten Ketchup ab 18!
Zielgruppe
Glühender Gustav ist der erste Ketchup ab 18!
Die Flasche besteht aus zwei Teilen.
1. Hälfte = Ketchup
2. Hälfte = Flambiersauce
Erst kommt der Ketchtup auf das Grillgut, danach die Flambiersauce.
Die Flambiersauce ist zum anzünden. Ein Karamellisierungseffekt entsteht.
Hier ein Video wie das ganze Funktioniert:
https://gluehender-gustav.de/pages/anleitung
Aufgabenstellung
Wir möchte für die Flasche einen Umkarton haben.
Der Umkarton soll auffällig sein und am besten das Produkt auf den ersten Blick erklären oder Interesse wecken.
Der Karton sollte nicht zu dunkel sein.
Es soll erkennbar sein, dass es sich um brennenden Ketchup handelt.
Vorn im Karton wird es einen Ausschnitt geben in diesem ist die Flasche zu sehen.
Wir sind gespannt auf Eure Ideen.
Seid gerne kreativ! Eigene Bilder über Bildkammer o.ä. können genutzt werden.
Feurige Grüße
Glühender Gustav

```html
<!DOCTYPE html>
<html lang="de">
<head>
<meta charset="utf-8">
<title>Glühender Gustav – Umkarton Ketchup &amp; Flambiersauce</title>
<link href="https://fonts.googleapis.com/css2?family=Cormorant+Garamond:wght@500;600&family=Crimson+Text:wght@400&display=swap" rel="stylesheet">
<style>
  :root {
    --stage: #e9e9e9;
    --ketchup-red: #b72d3a;
    --carton-black: #1d1d1d;
    --side-black: #0e0e0e;
    --gold: #d8b979;
    --gold-line: #c9a45e;
    --window: #e6e6e6;
    --accent-red: #c8202e;
    --flame-deep: #c4460f;
    --flame-bright: #f6b632;
  }
  * { margin: 0; padding: 0; box-sizing: border-box; }
  html, body { width: 1200px; height: 840px; overflow: hidden; }
  body {
    background: var(--stage);
    display: flex; align-items: center; justify-content: center;
    font-family: "Crimson Text", Georgia, serif;
  }
  .dieline { display: flex; box-shadow: 0 12px 30px rgba(0,0,0,.18); }

  /* Front panel */
  .panel-front {
    position: relative; width: 290px; height: 740px;
    background: linear-gradient(90deg, var(--ketchup-red) 0 47%, var(--carton-black) 47% 100%);
    overflow: hidden;
  }
  .brand-name {
    font-family: "Cormorant Garamond", Georgia, serif;
    font-weight: 600; color: var(--gold);
    text-transform: uppercase; text-align: center; line-height: .95;
    white-space: nowrap;
  }
  .panel-front .brand-name {
    position: absolute; top: 34px; left: 0; right: 0; font-size: 30px;
  }
  .flames {
    position: absolute;
    background: radial-gradient(closest-side, var(--flame-bright) 0%, var(--flame-deep) 50%, rgba(196,70,15,0) 100%);
    opacity: .9;
  }
  .flames-left { left: 20px; top: 190px; width: 70px; height: 440px; }
  .flames-right { left: 188px; top: 160px; width: 86px; height: 480px; }
  .window-frame { position: absolute; left: 0; top: 0; }
  .window-cutout {
    position: absolute; left: 67px; top: 178px; width: 142px; height: 437px;
    border-radius: 36px; background: var(--window);
    box-shadow: inset 0 4px 10px rgba(0,0,0,.15);
  }
  .product-title {
    position: absolute; left: 0; right: 0; top: 650px; text-align: center;
    font-family: "Cormorant Garamond", Georgia, serif; color: var(--gold);
    text-transform: uppercase;
  }
  .product-title .title-main { font-size: 26px; font-weight: 500; letter-spacing: 1px; line-height: 1; }
  .product-title .title-sub { font-size: 16px; font-weight: 500; letter-spacing: 1px; }
  .product-volume {
    position: absolute; left: 0; right: 0; top: 706px; text-align: center;
    font-size: 11.5px; color: var(--gold); letter-spacing: .3px;
  }

  /* Side panel */
  .panel-side {
    position: relative; width: 240px; height: 740px;
    background: var(--side-black); padding: 38px 20px 0;
    overflow: hidden;
  }
  .brand-story { font-size: 10.4px; line-height: 1.55; color: var(--gold); text-align: left; }
  .panel-side .brand-name { margin-top: 128px; font-size: 30px; }
  .side-title {
    margin-top: 56px; text-align: center; text-transform: uppercase;
    font-family: "Cormorant Garamond", Georgia, serif; font-weight: 500; line-height: 1.05;
  }
  .side-title .title-main { color: var(--accent-red); font-size: 26px; letter-spacing: 1px; }
  .side-title .title-sub { color: var(--gold); font-size: 18px; letter-spacing: 1px; }
</style>
</head>
<body>
  <main class="dieline">
    <section class="panel-front">
      <div class="brand-name">Glühender<br>Gustav</div>

      <div class="flames flames-left" role="img" aria-label="Foto lodernder Flammen links neben dem Sichtfenster"></div>
      <div class="flames flames-right" role="img" aria-label="Foto lodernder Flammen rechts neben dem Sichtfenster"></div>

      <svg class="window-frame" width="290" height="740" viewBox="0 0 290 740" aria-hidden="true">
        <path d="M56 176 Q56 160 72 158 Q120 150 140 140 Q160 150 208 158 Q224 160 224 176 V624 Q224 636 212 638 Q170 642 140 650 Q110 642 68 638 Q56 636 56 624 Z"
              fill="none" stroke="var(--gold-line)" stroke-width="1.4"/>
      </svg>
      <div class="window-cutout" aria-label="Sichtfenster auf die Flasche"></div>

      <div class="product-title">
        <div class="title-main">Ketchup</div>
        <div class="title-sub">Flambiersauce</div>
      </div>
      <p class="product-volume">100 ml Flambier Sauce + 180 ml Ketchup</p>
    </section>

    <section class="panel-side">
      <p class="brand-story">Da ich ein sehr geselliger und kultureller Typ bin, dessen Gedanken sich meistens nur ums Essen drehen, habe ich vor zwei Jahren eine Weltreise begonnen. In dieser Zeit bereiste ich 34 Länder auf sieben Kontinenten. Ich habe eine Menge unterschiedliche Menschen kennengelernt, die mein Leben und mein Wissen auf eine gewisse Weise verändert haben. Ich habe die unterschiedlichsten Kulturen getroffen und die Lebensart sowie Weise der Menschen miterlebt. Alle, die ich kennenlernen durfte, haben mich mit offenen Armen empfangen. Ich durfte bei ihnen wohnen, mit ihnen kochen und für kurze Zeit ein Teil ihres Lebens werden. Durch diese Erfahrungen habe ich gemerkt, dass ich für die Welt und das Reisen brenne. Ich möchte Euch erzählen, wie ich auf die Idee gekommen bin, den ersten brennenden Ketchup herzustellen, der den Geschmack meiner Lieblingsspirituosen mit dem meiner favorisierten Grillsaucen verbindet.</p>
      <div class="brand-name">Glühender<br>Gustav</div>
      <div class="side-title">
        <div class="title-main">Ketchup</div>
        <div class="title-sub">Flambiersauce</div>
      </div>
    </section>
  </main>
</body>
</html>
```